Verelto Services

Double sided business cards with color on front and black and white on back. I have basic ideas and graphics, but am looking for someone to take them to the next level

```html
<!DOCTYPE html>
<html lang="en">
<head>
<meta charset="utf-8">
<title>Verelto Services – Business Card</title>
<link rel="stylesheet" href="https://fonts.googleapis.com/css2?family=Montserrat:wght@500;700;800&family=Arimo:wght@400;700&display=swap">
<style>
  :root {
    --bg: #e4e4e4;
    --card: #ffffff;
    --green: #6bbd3a;
    --ink: #2b2b2b;
    --grey: #555555;
    --faint: #ececec;
    --black: #000000;
    --yellow: #f2d83b;
    --orange: #ee8a3a;
    --red: #e8322f;
    --pink: #c8479a;
    --teal: #6ccfa0;
    --lime: #7cc24a;
    --blue: #4aa0d8;
    --violet: #5b4fa6;
  }
  * { box-sizing: border-box; margin: 0; padding: 0; }
  html, body { width: 1200px; height: 802px; overflow: hidden; }
  body {
    background: var(--bg);
    font-family: "Arimo", Arial, sans-serif;
    position: relative;
  }
  .card {
    position: absolute;
    top: 246px;
    width: 540px;
    height: 310px;
    overflow: hidden;
    box-shadow: 0 6px 18px rgba(0,0,0,.18);
  }
  /* Front */
  .card-front { left: 45px; background: var(--card); }
  .front-band {
    position: absolute; left: 0; right: 0; bottom: 0; height: 12px;
    background: linear-gradient(90deg, var(--yellow), var(--orange), var(--red), var(--pink), var(--teal), var(--lime), var(--blue), var(--violet));
  }
  .front-tab {
    position: absolute; left: 0; bottom: 40px; width: 40px; height: 14px;
    background: var(--green);
  }
  .deco-circle { position: absolute; left: 268px; top: 18px; width: 240px; height: 240px; }
  .brand { position: absolute; left: 30px; top: 38px; display: flex; align-items: center; gap: 14px; }
  .brand-dot { width: 60px; height: 60px; border-radius: 50%; background: var(--green); opacity: .85; }
  .brand-name {
    font-family: "Montserrat", sans-serif; font-weight: 800; color: var(--green);
    font-size: 30px; letter-spacing: 1px; line-height: 1; text-transform: uppercase;
  }
  .brand-sub {
    display: flex; align-items: center; gap: 6px; margin-top: 4px;
    font-family: "Montserrat", sans-serif; font-weight: 700; color: var(--ink);
    font-size: 13px; letter-spacing: 3px;
  }
  .brand-sub::before { content: ""; width: 46px; height: 1px; background: var(--ink); }
  .brand-sub::after { content: ""; flex: 1; width: 90px; height: 1px; background: var(--ink); }
  .person { position: absolute; left: 40px; top: 138px; }
  .person-name {
    font-family: "Montserrat", sans-serif; font-weight: 700; color: var(--green);
    font-size: 21px; text-transform: uppercase;
  }
  .person-role { color: var(--grey); font-size: 15px; margin-top: 2px; }
  .contacts { position: absolute; left: 40px; top: 200px; list-style: none; }
  .contacts li { display: flex; align-items: center; gap: 10px; font-size: 15px; color: var(--ink); margin-bottom: 6px; }
  .contacts svg { width: 14px; height: 14px; fill: var(--green); }
  .address {
    position: absolute; right: 32px; top: 60px; text-align: right;
    font-size: 14px; line-height: 1.35; color: var(--ink);
  }
  /* Back */
  .card-back {
    left: 615px;
    background:
      linear-gradient(160deg, rgba(0,0,0,.75) 0%, rgba(0,0,0,.25) 25%, rgba(0,0,0,0) 45%),
      linear-gradient(90deg, var(--yellow) 0%, var(--orange) 10%, var(--red) 22%, var(--pink) 36%, var(--teal) 50%, var(--lime) 64%, var(--blue) 82%, var(--violet) 100%);
  }
  .back-mark {
    position: absolute; left: 50%; top: 42px; transform: translateX(-50%);
    display: flex; align-items: center; gap: 12px;
  }
  .back-mark-circle { width: 70px; height: 70px; border-radius: 50%; background: var(--black); }
  .back-mark-name {
    font-family: "Montserrat", sans-serif; font-weight: 800; font-size: 30px;
    color: var(--black); text-transform: uppercase; letter-spacing: 1px;
  }
  .tagline {
    position: absolute; left: 0; right: 0; top: 200px; text-align: center;
    font-family: "Arimo", Arial, sans-serif; font-weight: 700; font-size: 17px;
    line-height: 1.25; color: var(--black); text-transform: uppercase;
  }
</style>
</head>
<body>
  <section class="card card-front">
    <svg class="deco-circle" viewBox="0 0 240 240" role="img" aria-label="Faint decorative circle area">
      <circle cx="120" cy="120" r="118" fill="var(--faint)"/>
    </svg>
    <div class="brand">
      <span class="brand-dot"></span>
      <div>
        <div class="brand-name">Verelto</div>
        <div class="brand-sub">SERVICES</div>
      </div>
    </div>
    <div class="person">
      <div class="person-name">Daniel Morrow</div>
      <div class="person-role">Manager</div>
    </div>
    <ul class="contacts">
      <li><svg viewBox="0 0 24 24"><path d="M6.6 10.8a15.1 15.1 0 0 0 6.6 6.6l2.2-2.2a1 1 0 0 1 1-.25 11.4 11.4 0 0 0 3.6.57 1 1 0 0 1 1 1V20a1 1 0 0 1-1 1A17 17 0 0 1 3 4a1 1 0 0 1 1-1h3.5a1 1 0 0 1 1 1c0 1.25.2 2.45.57 3.57a1 1 0 0 1-.25 1z"/></svg>949-555-0148</li>
      <li><svg viewBox="0 0 24 24"><path d="M2 5h20v14H2z M2 5l10 8 10-8" /></svg>youremail@mailbox.com</li>
      <li><svg viewBox="0 0 24 24"><circle cx="12" cy="12" r="10"/></svg>www.yourwebsite.com</li>
    </ul>
    <div class="address">Your Address<br>City, State, Zip 0000</div>
    <div class="front-tab"></div>
    <div class="front-band"></div>
  </section>

  <section class="card card-back">
    <div class="back-mark">
      <span class="back-mark-circle"></span>
      <span class="back-mark-name">Verelto</span>
    </div>
    <p class="tagline">A Curated Experience<br>All That Is Promised Is Clarity</p>
  </section>
</body>
</html>
```